Willowmere Equine Sanctuary Flyer Urgent

Willowmere Equine Sanctuary

Rescue • Rehabilitation • Sanctuary

Willowmere Equine Sanctuary provides a safe and ethical refuge for horses, ponies and donkeys who have nowhere else to go. Some arrive needing rehabilitation and careful retraining, while others find permanent sanctuary here due to age, injury or behavioural needs.

Our mission is simple: to improve the physical and psychological wellbeing of every animal in our care.

At Willowmere we focus on:
• Rescue and rehabilitation of horses in need
• Lifetime sanctuary for those who cannot be rehomed
• Education and advocacy for responsible horse care
• Equine rehabilitation services to help horses recover and thrive

Sponsor a Horse

One of the most meaningful ways to support our work is by sponsoring one of our residents. Each horse, pony or donkey only has one sponsor!

Your sponsorship helps provide:
• Hay and feed
• Veterinary care
• Hoof trimming and routine health care
• Rugs, shelter and daily care

Many of our horses will live out their lives here, and sponsorship ensures they are safe, well fed and cared for every single day.

Sponsorship starts from $15 - $25 per week / $60 -$100 per month.

How You Can Help

• Sponsor a horse
• Make a donation
• Share our work with others

Your support helps us continue to say yes to horses who need a second chance.

📍 Willowmere Park, Victoria
📧 clara@willowmerepark-example.org

📞 0400 519 627

Font styles to use
Serif
Sans Serif

Colors
F0912C
F2A743
F7CA91
FBE8D2
FDF5EE
EE7325
F08F49
F5BC92
FAE3D3
FDF4ED

Requirements
Should not have
• Photos not provided by Willowmere

```html
<!DOCTYPE html>
<html lang="en">
<head>
<meta charset="utf-8">
<title>Willowmere Equine Sanctuary – Sponsorship Flyer</title>
<link href="https://fonts.googleapis.com/css2?family=Cinzel:wght@400;700;800&family=Open+Sans:wght@400;600;700&display=swap" rel="stylesheet">
<style>
  :root{
    --orange:#EE7325;
    --orange-warm:#F0912C;
    --mission-orange:#F08F49;
    --peach:#F7CA91;
    --cream:#FBE8D2;
    --blue:#3B4FA6;
    --ink:#1f1f1f;
    --white:#ffffff;
    --page:#f3f3f3;
  }
  *{box-sizing:border-box;margin:0;padding:0}
  html,body{width:1200px;height:1200px;overflow:hidden;background:var(--page)}
  .stage{position:relative;width:1200px;height:1200px}
  .flyer{
    position:absolute;left:189px;top:20px;width:1108px;height:1566px;
    transform:scale(0.7407);transform-origin:top left;
    background:var(--white);overflow:hidden;
    font-family:"Open Sans",sans-serif;color:var(--ink);
  }
  .flyer-shapes{position:absolute;inset:0}
  .abs{position:absolute}
  .title{
    left:0;width:1108px;top:82px;text-align:center;color:var(--white);
    font-family:"Cinzel",serif;font-weight:800;font-size:58px;line-height:70px;text-transform:uppercase;
  }
  .tagline{left:0;width:1108px;top:218px;text-align:center;color:var(--white);font-weight:700;font-size:29px}
  .intro{left:150px;width:820px;top:266px;text-align:center;color:var(--white);font-size:19px;line-height:24.5px}
  .sponsor-badge{left:55px;top:460px;width:330px;text-align:center;color:var(--white)}
  .sponsor-badge .lead{font-weight:600;font-size:30px;line-height:38px}
  .sponsor-badge .price{font-weight:700;font-size:40px;line-height:44px;margin-top:8px}
  .sponsor-badge .per{font-size:30px;line-height:30px}
  .sponsor-badge .price.month{margin-top:8px}
  .sponsor-pitch{left:64px;top:778px;width:315px;color:var(--white);font-weight:700;font-size:20px;line-height:26px}
  .provides-title{left:62px;top:962px;color:var(--white);font-family:"Cinzel",serif;font-weight:800;font-size:30px;line-height:41px}
  .provides-list{left:64px;top:1052px;width:380px;list-style:none;color:var(--white);font-weight:700;font-size:24px;line-height:30px}
  .provides-list li{position:relative;padding-left:30px;margin-bottom:4px}
  .provides-list svg{position:absolute;left:0;top:9px;width:18px;height:18px}
  .mission{left:440px;width:600px;top:465px;text-align:center}
  .mission-head{font-family:"Cinzel",serif;font-weight:800;font-size:42px;color:var(--mission-orange);line-height:50px}
  .mission-body{font-family:"Cinzel",serif;font-size:28px;line-height:37px}
  .divider{left:570px;top:637px;width:320px;border-top:2px dotted #777}
  .focus-title{left:485px;top:655px;color:var(--blue);font-weight:700;font-size:26px}
  .focus-list{left:485px;top:693px;width:600px;list-style:none;font-size:22px;line-height:35.5px}
  .focus-list li{position:relative;padding-left:24px}
  .focus-list svg{position:absolute;left:0;top:12px;width:15px;height:15px}
  .help-box{
    left:542px;top:902px;width:444px;height:193px;background:var(--cream);
    border:8px solid var(--peach);border-radius:8px;text-align:center;padding-top:18px;
  }
  .help-box h2{font-weight:600;font-size:30px;line-height:40px}
  .help-box ul{list-style:none;font-weight:700;font-size:22px;line-height:27px;margin-top:6px}
  .closing{left:505px;width:520px;top:1133px;text-align:center;font-family:"Cinzel",serif;font-weight:800;font-size:24px;line-height:30px}
  .photo{border:6px solid var(--cream)}
  .footer-line{left:380px;width:728px;text-align:center;color:var(--white);font-weight:700;white-space:nowrap}
  .footer-line svg{display:inline-block;vertical-align:middle;margin-right:6px}
  .footer-place{top:1476px;font-size:30px}
  .footer-contact{top:1522px;font-size:23px}
  .footer-contact .gap{display:inline-block;width:18px}
</style>
</head>
<body>
<div class="stage">
  <div class="flyer">
    <svg class="flyer-shapes" width="1108" height="1566" viewBox="0 0 1108 1566">
      <defs>
        <linearGradient id="headerTone" x1="0" y1="0" x2="0" y2="1">
          <stop offset="0" stop-color="#b88a45"/>
          <stop offset="0.5" stop-color="#c99a55"/>
          <stop offset="1" stop-color="#a8894f"/>
        </linearGradient>
        <linearGradient id="herdTone" x1="0" y1="0" x2="1" y2="1">
          <stop offset="0" stop-color="#6f4a36"/>
          <stop offset="0.6" stop-color="#4a2e22"/>
          <stop offset="1" stop-color="#7a5a48"/>
        </linearGradient>
      </defs>
      <path d="M0 0H1108V300Q820 430 560 425Q270 420 0 290Z" fill="url(#headerTone)" role="img" aria-label="Photo of horses grazing in a sunlit paddock"/>
      <path d="M430 432Q800 430 1108 302V362Q800 460 450 442Z" fill="var(--orange)"/>
      <path d="M0 470Q160 370 360 440Q440 520 455 760Q470 1100 380 1566H0Z" fill="var(--orange)"/>
      <path d="M0 375Q60 395 110 425L90 450Q50 430 0 410Z" fill="var(--blue)"/>
      <path d="M325 695Q430 800 455 965Q420 830 305 712Z" fill="var(--blue)"/>
      <circle cx="215" cy="570" r="185" fill="var(--orange)"/>
      <circle cx="215" cy="570" r="165" fill="var(--blue)"/>
      <path d="M0 1290Q120 1230 220 1260Q320 1210 390 1260L385 1566H0Z" fill="url(#herdTone)" role="img" aria-label="Photo of two brown horses standing head to head"/>
      <rect x="380" y="1466" width="728" height="100" fill="var(--orange-warm)"/>
    </svg>

    <h1 class="abs title">Willowmere Equine<br>Sanctuary</h1>
    <p class="abs tagline">RESCUE • REHABILITATION • SANCTUARY</p>
    <p class="abs intro">Willowmere Equine Sanctuary provides a safe and ethical refuge for horses, ponies and donkeys who have nowhere else to go. Some arrive needing rehabilitation and careful retraining, while others find permanent sanctuary here due to age, injury or behavioural needs.</p>

    <div class="abs sponsor-badge">
      <p class="lead">SPONSORSHIP<br>STARTS FROM</p>
      <p class="price">$15 - $25</p>
      <p class="per">per week</p>
      <p class="price month">$60 -$100</p>
      <p class="per">per month.</p>
    </div>

    <p class="abs sponsor-pitch">One of the most meaningful ways to support our work is by sponsoring one of our residents. Each horse, pony or donkey only has one sponsor!</p>

    <h2 class="abs provides-title">Your Sponsorship<br>Helps Provide:</h2>
    <ul class="abs provides-list">
      <li><svg viewBox="0 0 18 18"><rect x="1.5" y="3" width="13" height="13" rx="2" fill="none" stroke="#fff" stroke-width="1.8"/><path d="M5 9l3 3 8-9" fill="none" stroke="#fff" stroke-width="2"/></svg>Hay and feed</li>
      <li><svg viewBox="0 0 18 18"><rect x="1.5" y="3" width="13" height="13" rx="2" fill="none" stroke="#fff" stroke-width="1.8"/><path d="M5 9l3 3 8-9" fill="none" stroke="#fff" stroke-width="2"/></svg>Veterinary care</li>
      <li><svg viewBox="0 0 18 18"><rect x="1.5" y="3" width="13" height="13" rx="2" fill="none" stroke="#fff" stroke-width="1.8"/><path d="M5 9l3 3 8-9" fill="none" stroke="#fff" stroke-width="2"/></svg>Hoof trimming and routine health care</li>
      <li><svg viewBox="0 0 18 18"><rect x="1.5" y="3" width="13" height="13" rx="2" fill="none" stroke="#fff" stroke-width="1.8"/><path d="M5 9l3 3 8-9" fill="none" stroke="#fff" stroke-width="2"/></svg>Rugs, shelter and daily care</li>
    </ul>

    <div class="abs mission">
      <h2 class="mission-head">Our Mission is Simple:</h2>
      <p class="mission-body">TO IMPROVE THE PHYSICAL AND PSYCHOLOGICAL WELLBEING OF EVERY ANIMAL IN OUR CARE.</p>
    </div>
    <div class="abs divider"></div>

    <h2 class="abs focus-title">AT WILLOWMERE WE FOCUS ON:</h2>
    <ul class="abs focus-list">
      <li><svg viewBox="0 0 15 15"><circle cx="7" cy="8" r="6" fill="none" stroke="#333" stroke-width="1.3"/><path d="M4 8l2.5 2.5L13 3" fill="none" stroke="#333" stroke-width="1.5"/></svg>Rescue and rehabilitation of horses in need</li>
      <li><svg viewBox="0 0 15 15"><circle cx="7" cy="8" r="6" fill="none" stroke="#333" stroke-width="1.3"/><path d="M4 8l2.5 2.5L13 3" fill="none" stroke="#333" stroke-width="1.5"/></svg>Lifetime sanctuary for those who cannot be rehomed</li>
      <li><svg viewBox="0 0 15 15"><circle cx="7" cy="8" r="6" fill="none" stroke="#333" stroke-width="1.3"/><path d="M4 8l2.5 2.5L13 3" fill="none" stroke="#333" stroke-width="1.5"/></svg>Education and advocacy for responsible horse care</li>
      <li><svg viewBox="0 0 15 15"><circle cx="7" cy="8" r="6" fill="none" stroke="#333" stroke-width="1.3"/><path d="M4 8l2.5 2.5L13 3" fill="none" stroke="#333" stroke-width="1.5"/></svg>Equine rehabilitation services to help horses<br>recover and thrive</li>
    </ul>

    <div class="abs help-box">
      <h2>HOW YOU CAN HELP</h2>
      <ul>
        <li>• Sponsor a horse</li>
        <li>• Make a donation</li>
        <li>• Share our work with others</li>
      </ul>
    </div>

    <p class="abs closing">Your support helps us continue to say yes to horses who need a second chance.</p>

    <div class="abs photo" style="left:466px;top:1237px;width:291px;height:196px;background:linear-gradient(180deg,#8d9a7a 0%,#5a4634 55%,#9c8e78 100%)" role="img" aria-label="Photo of a group of miniature ponies in a paddock"></div>
    <div class="abs photo" style="left:770px;top:1235px;width:290px;height:198px;background:linear-gradient(135deg,#3f6a3a 0%,#8a4a26 50%,#5a3220 100%)" role="img" aria-label="Photo of two chestnut horses nuzzling"></div>

    <p class="abs footer-line footer-place"><svg width="26" height="30" viewBox="0 0 26 30"><path d="M13 1C6.5 1 2 5.8 2 11.5 2 19 13 29 13 29S24 19 24 11.5C24 5.8 19.5 1 13 1Z" fill="#fff"/><circle cx="13" cy="11.5" r="4.5" fill="var(--orange-warm)"/></svg>Willowmere Park, Victoria</p>
    <p class="abs footer-line footer-contact"><svg width="18" height="20" viewBox="0 0 20 22"><path d="M4 1l4 5-2.5 2.5c1.2 3 3.5 5.6 6.5 7L14.5 13l5 4-2.5 4C9 21 1 12 1 4Z" fill="#fff"/></svg>0400 519 627<span class="gap"></span><svg width="20" height="15" viewBox="0 0 22 16"><rect x="1" y="1" width="20" height="14" fill="none" stroke="#fff" stroke-width="2"/><path d="M1 1l10 8 10-8" fill="none" stroke="#fff" stroke-width="2"/></svg>clara@willowmerepark-example.org</p>
  </div>
</div>
</body>
</html>
```